Banner Ad to promote Youth Cycling Camps

We need a 728 x 90 banner ad to promote some youth cycling camps. There are 2 different camps - a road camp where they learn to ride their bikes on the roads and a mountain bike camp. The camps teach bike handling skills and racing tactics.

Target Market(s)

Parents of youth ages 7-17

Industry/Entity Type

Non-Profit

Font styles to use
Sans Serif

Requirements
Must have
• Logo
• Dates - Road Camp May 5-7, 2017
• - Mountain Bike Camp July 14-16, 2017
• website - quadrapedalcup.org
• be 728 x 90
Nice to have
• Animated - would like it to rotate with 3 slides - 1 a focus on both camps, 1 on road camp, 1 on mountain bike camp

```html
<!DOCTYPE html>
<html lang="en">
<head>
<meta charset="utf-8">
<title>Youth Cycling Camps – Banner Set</title>
<link href="https://fonts.googleapis.com/css2?family=Bebas+Neue&display=swap" rel="stylesheet">
<style>
  :root {
    --page: #efefef;
    --white: #ffffff;
    --ink: #111111;
    --mtb-blue: rgba(78, 146, 170, 0.88);
    --road-green: rgba(142, 190, 92, 0.9);
    --date-yellow: #f4e40c;
  }
  html, body {
    margin: 0;
    width: 1200px;
    height: 1000px;
    overflow: hidden;
    background: var(--page);
  }
  .banner-set { position: relative; width: 1200px; height: 1000px; }
  .banner {
    position: absolute;
    left: 236px;
    width: 728px;
    height: 90px;
    display: block;
    filter: drop-shadow(0 8px 10px rgba(0,0,0,0.22));
  }
  .banner--both { top: 165px; }
  .banner--mtb { top: 455px; }
  .banner--road { top: 745px; }
  .banner text { font-family: "Bebas Neue", "Oswald", sans-serif; }
  .label { fill: var(--white); font-size: 22px; letter-spacing: 2.6px; }
  .date { fill: var(--date-yellow); font-size: 21px; letter-spacing: 2px; }
  .url { fill: var(--ink); font-size: 12px; letter-spacing: 1.3px; }
  .brand { fill: var(--ink); font-size: 17px; letter-spacing: 1.2px; }
  .panel { fill: var(--white); }
  .mtb-band { fill: var(--mtb-blue); }
  .road-band { fill: var(--road-green); }
</style>
</head>
<body>
<main class="banner-set">

  <svg class="banner banner--both" viewBox="0 0 728 90" xmlns="http://www.w3.org/2000/svg">
    <defs>
      <linearGradient id="photoBoth" x1="0" y1="0" x2="1" y2="0">
        <stop offset="0" stop-color="#7c6e62"/>
        <stop offset="0.45" stop-color="#a08a72"/>
        <stop offset="0.7" stop-color="#6b6c66"/>
        <stop offset="1" stop-color="#9a9a94"/>
      </linearGradient>
    </defs>
    <rect x="0" y="0" width="728" height="90" class="panel"/>
    <polygon points="126,0 728,0 728,90 176,90" fill="url(#photoBoth)" role="img" aria-label="Photo of young riders in a group ride and a road cyclist riding past cones"/>
    <polygon points="126,0 404,0 452,45 150,45" class="mtb-band"/>
    <polygon points="432,45 728,45 728,90 476,90" class="road-band"/>
    <polygon points="682,0 728,0 728,90" class="panel"/>
    <text class="label" x="283" y="30" text-anchor="middle">Mountain Bike Camp</text>
    <text class="label" x="577" y="75" text-anchor="middle">Road Bike Camp</text>
    <text class="brand" x="75" y="42" text-anchor="middle">Pedalworks Youth</text>
    <text class="url" x="9" y="83">http://quadrapedalcup.org/</text>
  </svg>

  <svg class="banner banner--mtb" viewBox="0 0 728 90" xmlns="http://www.w3.org/2000/svg">
    <defs>
      <linearGradient id="photoMtb" x1="0" y1="0" x2="1" y2="0">
        <stop offset="0" stop-color="#5e5a55"/>
        <stop offset="0.5" stop-color="#8c7a66"/>
        <stop offset="1" stop-color="#b39f84"/>
      </linearGradient>
    </defs>
    <rect x="0" y="0" width="728" height="90" class="panel"/>
    <polygon points="126,0 728,0 728,90 176,90" fill="url(#photoMtb)" role="img" aria-label="Photo of young riders on a dirt trail"/>
    <polygon points="126,0 678,0 705,45 150,45" class="mtb-band"/>
    <polygon points="682,0 728,0 728,90" class="panel"/>
    <text class="label" x="283" y="30" text-anchor="middle">Mountain Bike Camp</text>
    <text class="date" x="400" y="75">Friday to Sunday, July 14-16, 2017</text>
    <text class="brand" x="75" y="42" text-anchor="middle">Pedalworks Youth</text>
    <text class="url" x="9" y="83">http://quadrapedalcup.org/</text>
  </svg>

  <svg class="banner banner--road" viewBox="0 0 728 90" xmlns="http://www.w3.org/2000/svg">
    <defs>
      <linearGradient id="photoRoad" x1="0" y1="0" x2="1" y2="0">
        <stop offset="0" stop-color="#7a4a3a"/>
        <stop offset="0.4" stop-color="#6a6760"/>
        <stop offset="1" stop-color="#8e8e88"/>
      </linearGradient>
    </defs>
    <rect x="0" y="0" width="728" height="90" class="panel"/>
    <polygon points="126,0 728,0 728,90 176,90" fill="url(#photoRoad)" role="img" aria-label="Photo of young road cyclists riding through a cone course"/>
    <polygon points="150,45 728,45 728,90 176,90" class="road-band"/>
    <polygon points="682,0 728,0 728,90" class="panel"/>
    <text class="date" x="167" y="30">Friday to Sunday, May 5,6,7, 2017</text>
    <text class="label" x="577" y="75" text-anchor="middle">Road Bike Camp</text>
    <text class="brand" x="75" y="42" text-anchor="middle">Pedalworks Youth</text>
    <text class="url" x="9" y="83">http://quadrapedalcup.org/</text>
  </svg>

</main>
</body>
</html>
```